Business Card Design

we specialise in supply of custom uniforms - teamwear to Schools and sporting clubs, see our website: www.harbourkitcove.com.au, our main corporate colour is black and white, with small amount of gold/yellow

Industry/Entity Type

Business

Contact Information for Business Card

Harbour Kit Cove
Travis Okafor
Ph 03 6218 5097
Mobile 0462 318 740
email: travis@harbourkitcove.com.au
www.harbourkitcove.com.au
like us on facebook

Requirements
Must have
• modern look & feel

```html
<!DOCTYPE html>
<html lang="en">
<head>
<meta charset="utf-8">
<title>Harbour Kit Cove – Business Card</title>
<link rel="stylesheet" href="https://fonts.googleapis.com/css2?family=Cinzel:wght@500&family=Open+Sans:wght@400&family=Raleway:wght@400&display=swap">
<style>
  :root {
    --page-bg: #2b2b2b;
    --card-black: #050607;
    --brand-gold: #fcd500;
    --text-white: #f4f4f4;
    --text-dark: #0b0b0b;
  }
  html, body {
    margin: 0;
    width: 1200px;
    height: 798px;
    overflow: hidden;
    background: var(--page-bg);
  }
  .business-card {
    position: absolute;
    left: 150px;
    top: 142px;
    width: 900px;
    height: 514px;
    background: var(--card-black);
    overflow: hidden;
    font-family: "Open Sans", sans-serif;
    color: var(--text-white);
  }
  .card-bands {
    position: absolute;
    inset: 0;
  }
  .card-bands .band { fill: var(--brand-gold); }
  .holder {
    position: absolute;
    top: 24px;
    right: 58px;
    text-align: center;
  }
  .holder-name {
    font-family: "Raleway", sans-serif;
    font-size: 34px;
    letter-spacing: 0.5px;
    margin: 0;
    font-weight: 400;
  }
  .holder-role {
    font-size: 18px;
    margin: 4px 0 0;
  }
  .company-name {
    position: absolute;
    top: 214px;
    left: 190px;
    margin: 0;
    font-family: "Cinzel", serif;
    font-weight: 500;
    font-size: 46px;
    letter-spacing: 1px;
    color: var(--text-dark);
    text-transform: uppercase;
  }
  .contact-list {
    position: absolute;
    left: 46px;
    top: 322px;
    margin: 0;
    padding: 0;
    list-style: none;
  }
  .contact-item {
    display: flex;
    align-items: center;
    height: 40px;
    font-size: 20px;
    letter-spacing: 0.5px;
  }
  .contact-item.email { font-size: 18px; }
  .contact-icon {
    width: 22px;
    height: 22px;
    margin-right: 26px;
    fill: none;
    stroke: var(--brand-gold);
    stroke-width: 1.8;
  }
  .contact-icon .solid { fill: var(--brand-gold); stroke: none; }
  .website {
    position: absolute;
    right: 28px;
    top: 388px;
    margin: 0;
    font-size: 18px;
    letter-spacing: 0.3px;
  }
</style>
</head>
<body>
  <article class="business-card">
    <svg class="card-bands" width="900" height="514" viewBox="0 0 900 514" aria-hidden="true">
      <polygon class="band band-top" points="0,64 432,64 392,104 0,104"/>
      <rect class="band band-main" x="0" y="196" width="900" height="92"/>
      <polygon class="band band-bottom" points="642,420 900,420 900,482 590,482"/>
    </svg>

    <header class="holder">
      <h2 class="holder-name">Travis Okafor</h2>
      <p class="holder-role">Sales manager</p>
    </header>

    <h1 class="company-name">Harbour Kit Cove</h1>

    <ul class="contact-list">
      <li class="contact-item email">
        <svg class="contact-icon" viewBox="0 0 22 22" aria-hidden="true">
          <rect x="2" y="5" width="18" height="12"/>
          <polyline points="2,5 11,12 20,5"/>
        </svg>
        travis@harbourkitcove.com.au
      </li>
      <li class="contact-item mobile">
        <svg class="contact-icon" viewBox="0 0 22 22" aria-hidden="true">
          <rect x="6" y="2" width="10" height="18" rx="1.5"/>
          <rect class="solid" x="8" y="4.5" width="6" height="9"/>
        </svg>
        0462 318 740
      </li>
      <li class="contact-item phone">
        <svg class="contact-icon" viewBox="0 0 22 22" aria-hidden="true">
          <path class="solid" d="M5 3 L8.5 3 L10 7.5 L7.8 9.2 C9 12 10.5 13.6 13 14.6 L14.6 12.4 L19 14 L19 17.5 C19 18.6 18 19.5 16.8 19.3 C10 18.4 4.2 12.6 3.2 5.6 C3 4.2 3.8 3 5 3 Z"/>
        </svg>
        03 6218 5097
      </li>
      <li class="contact-item fax">
        <svg class="contact-icon" viewBox="0 0 22 22" aria-hidden="true">
          <rect x="6" y="2.5" width="10" height="6"/>
          <rect class="solid" x="2.5" y="8" width="17" height="8" rx="1"/>
          <rect x="6" y="13" width="10" height="6.5"/>
        </svg>
        03 6274 3860
      </li>
    </ul>

    <p class="website">www.harbourkitcove.com.au</p>
  </article>
</body>
</html>
```